Business Card Design Project

WE NEED A CARD WITH THE NAME AND LOGO IN ONE SIDE AND THE ODER JUST THE INFORMATIONS LIKE NAME, E-MAIL, PHONE AND SITE. I HAVE A IDEA OF THE CARD ALL BLACK AND JUST COLLOORS IN THE LOGO AND INFORMATIONS. WE WANT SANTHING SIMPLE AND ELEGANT. SAMETHING NEW WICTH PASS CONFIANCE.
Updates

I HAVE UP DATE THE INFORMATIONS OF WAHT WE NEED. THNKSĀ 

Target Market(s)

COMPANY WHO ORGANIZE BIG CORPORATIVE EVENTS.

Industry/Entity Type

Business

Requirements
Should not have
• MUCH INFORMATION.

```html
<!DOCTYPE html>
<html lang="pt">
<head>
<meta charset="utf-8">
<title>KORA – Business Card</title>
<link rel="stylesheet" href="https://fonts.googleapis.com/css2?family=Questrial&display=swap">
<style>
  :root {
    --backdrop: #2a2a2b;
    --card: #ffffff;
    --card-shade: #f1f1f1;
    --orange: #f2671f;
    --grey-text: #6f6f73;
    --corner: 78px;
  }
  * { box-sizing: border-box; margin: 0; padding: 0; }
  html, body {
    width: 1200px;
    height: 900px;
    overflow: hidden;
    background: var(--backdrop);
    font-family: "Questrial", "Helvetica Neue", Arial, sans-serif;
  }
  .stage {
    width: 1200px;
    height: 900px;
    display: flex;
    flex-direction: column;
    align-items: center;
    justify-content: center;
    gap: 56px;
  }
  .card {
    width: 630px;
    height: 360px;
    background: linear-gradient(135deg, var(--card) 60%, var(--card-shade));
    border-radius: var(--corner) 6px var(--corner) 6px;
    position: relative;
    box-shadow: 0 10px 30px rgba(0,0,0,.45);
  }

  /* Front: brand name */
  .card--front {
    display: flex;
    align-items: center;
    justify-content: center;
  }
  .brand {
    display: flex;
    align-items: center;
    gap: 16px;
    color: var(--orange);
  }
  .brand__dot {
    width: 44px;
    height: 44px;
    border-radius: 50%;
    background: var(--orange);
  }
  .brand__name {
    font-size: 64px;
    line-height: 1;
    letter-spacing: 1px;
  }

  /* Back: contact */
  .card--back {
    display: flex;
    align-items: center;
    padding: 0 56px 0 64px;
    gap: 48px;
  }
  .brand-mark {
    display: flex;
    align-items: center;
    gap: 12px;
    color: var(--orange);
    flex-shrink: 0;
    width: 200px;
  }
  .brand-mark__dot {
    width: 34px;
    height: 34px;
    border-radius: 50%;
    background: var(--orange);
  }
  .brand-mark__name {
    font-size: 46px;
    line-height: 1;
    letter-spacing: 1px;
  }
  .contact { color: var(--grey-text); }
  .contact__name {
    color: var(--orange);
    font-size: 30px;
    line-height: 1.05;
  }
  .contact__role {
    color: var(--orange);
    font-size: 19px;
    margin-bottom: 20px;
  }
  .contact__list { list-style: none; }
  .contact__item {
    display: flex;
    align-items: center;
    gap: 12px;
    font-size: 17px;
    height: 30px;
  }
  .contact__icon {
    width: 24px;
    height: 24px;
    flex-shrink: 0;
  }
</style>
</head>
<body>
<main class="stage">

  <section class="card card--front" aria-label="Card front">
    <div class="brand">
      <span class="brand__dot" aria-hidden="true"></span>
      <span class="brand__name">KORA</span>
    </div>
  </section>

  <section class="card card--back" aria-label="Card back">
    <div class="brand-mark">
      <span class="brand-mark__dot" aria-hidden="true"></span>
      <span class="brand-mark__name">KORA</span>
    </div>
    <div class="contact">
      <p class="contact__name">Example Name</p>
      <p class="contact__role">Position</p>
      <ul class="contact__list">
        <li class="contact__item">
          <svg class="contact__icon" viewBox="0 0 24 24" aria-hidden="true">
            <circle cx="12" cy="12" r="11" fill="none" stroke="#f2671f" stroke-width="1.4"/>
            <rect x="8.5" y="5.5" width="7" height="13" rx="1.2" fill="none" stroke="#f2671f" stroke-width="1.4"/>
            <line x1="10.5" y1="16" x2="13.5" y2="16" stroke="#f2671f" stroke-width="1.2"/>
          </svg>
          <span>123 456 789</span>
        </li>
        <li class="contact__item">
          <svg class="contact__icon" viewBox="0 0 24 24" aria-hidden="true">
            <circle cx="12" cy="12" r="11" fill="none" stroke="#f2671f" stroke-width="1.4"/>
            <circle cx="12" cy="12" r="6.5" fill="none" stroke="#f2671f" stroke-width="1.2"/>
            <ellipse cx="12" cy="12" rx="2.8" ry="6.5" fill="none" stroke="#f2671f" stroke-width="1.1"/>
            <line x1="5.5" y1="12" x2="18.5" y2="12" stroke="#f2671f" stroke-width="1.1"/>
          </svg>
          <span>www.koraeventos.com</span>
        </li>
        <li class="contact__item">
          <svg class="contact__icon" viewBox="0 0 24 24" aria-hidden="true">
            <circle cx="12" cy="12" r="11" fill="none" stroke="#f2671f" stroke-width="1.4"/>
            <rect x="6" y="8" width="12" height="8.5" fill="none" stroke="#f2671f" stroke-width="1.3"/>
            <polyline points="6,8 12,13 18,8" fill="none" stroke="#f2671f" stroke-width="1.3"/>
          </svg>
          <span>info@koraeventos.com</span>
        </li>
        <li class="contact__item">
          <svg class="contact__icon" viewBox="0 0 24 24" aria-hidden="true">
            <circle cx="12" cy="12" r="11" fill="#f2671f"/>
            <path d="M12 5.5a4.3 4.3 0 0 0-4.3 4.3c0 3.2 4.3 8.2 4.3 8.2s4.3-5 4.3-8.2A4.3 4.3 0 0 0 12 5.5z" fill="#fff"/>
            <circle cx="12" cy="9.8" r="1.6" fill="#f2671f"/>
          </svg>
          <span>Address Line here 1234</span>
        </li>
      </ul>
    </div>
  </section>

</main>
</body>
</html>
```